Accounting Practice Business Card Design

I have a logo I am happy for you to use in the design of the Business Card.
You can edit and change colours as you please, I am not fixated on it.
I am looking for a modern and clean overall feel for the finished design.

The business is a small accounting practice who thrives on word of mouth referrals and this card will be given to all current and prospect clients.

Industry/Entity Type

Accountant

Contact Information for Business Card

Marcus Elwin
Level 5, 8 Corvale Ridge Road
ASHGROVE RISE VIC 3187
Phone: 9481 3057
Email: melwin@mrfaccountants.com.au
Web: www.mrfaccountants.com.au

Font styles to use
Serif
Sans Serif

Colors
0555a3
3277b5
85acd3
0393ce
33a6d7
85cae6
00a990
33b8a4
9bcb3c

Requirements
Must have
• "The end to your tax problems begin with us"
• "A referral from you is our greatest compliment"
Nice to have
• Modern clean professional

```html
<!DOCTYPE html>
<html lang="en">
<head>
<meta charset="utf-8">
<title>MRF Accountants — Business Card</title>
<link rel="stylesheet" href="https://fonts.googleapis.com/css2?family=Open+Sans:wght@400;600;700;800&display=swap">
<style>
  :root {
    --bg: #2b2b2b;
    --card: #f6f6f6;
    --brand-blue: #1a5c9e;
    --brand-green: #4f8f26;
    --muted-blue: #6f89a8;
    --ink: #333333;
    --rule: #3f7a1f;
  }
  * { box-sizing: border-box; margin: 0; padding: 0; }
  html, body {
    width: 1200px; height: 997px; overflow: hidden;
    background: var(--bg);
    font-family: "Open Sans", Arial, sans-serif;
  }
  .stage {
    width: 1200px; height: 997px;
    display: flex; flex-direction: column; align-items: center; justify-content: center;
    gap: 40px;
  }
  .card {
    position: relative;
    width: 760px; height: 434px;
    background: var(--card);
    border-radius: 22px;
    overflow: hidden;
    box-shadow: 0 12px 30px rgba(0,0,0,.45);
  }
  .wordmark {
    font-weight: 800;
    color: var(--brand-blue);
    letter-spacing: 1px;
    text-transform: uppercase;
    white-space: nowrap;
    text-align: center;
  }

  /* Back side */
  .card--back .tagline-top {
    position: absolute; top: 40px; left: 0; right: 0; text-align: center;
    font-size: 15px; letter-spacing: 1.5px; color: var(--muted-blue);
  }
  .card--back .wordmark {
    position: absolute; top: 180px; left: 0; right: 0;
    font-size: 54px;
  }
  .card--back .tagline-bottom {
    position: absolute; bottom: 40px; left: 0; right: 0; text-align: center;
    font-size: 15px; letter-spacing: 1.5px; color: var(--brand-green);
  }
  .card--back .tagline-bottom strong { font-weight: 700; }

  /* Front side */
  .card--front .wordmark {
    position: absolute; top: 72px; left: 0; right: 0;
    font-size: 48px; line-height: 1.1;
  }
  .card--front .rule {
    position: absolute; top: 170px; left: 40px; right: 40px;
    height: 2px; background: var(--rule);
  }
  .person { position: absolute; top: 205px; left: 50px; }
  .person__name { font-size: 24px; font-weight: 700; color: var(--brand-blue); letter-spacing: .5px; }
  .person__title { font-size: 17px; color: var(--brand-green); font-weight: 600; margin-top: 2px; }
  .person__rule { width: 380px; height: 2px; background: var(--rule); margin-top: 8px; }
  .contacts { position: absolute; top: 300px; left: 50px; list-style: none; }
  .contacts li {
    display: flex; align-items: center; gap: 12px;
    font-size: 17px; color: var(--ink); margin-bottom: 8px;
  }
  .contacts svg { width: 18px; height: 18px; fill: #3a3a3a; }
  .band {
    position: absolute; bottom: 0; height: 44px;
    display: flex; align-items: center; color: #fff; font-size: 16px;
    white-space: nowrap;
  }
  .band--address { left: 0; width: 63%; background: var(--brand-green); padding-left: 50px; }
  .band--web { right: 0; width: 37%; background: var(--brand-blue); justify-content: center; }
</style>
</head>
<body>
<main class="stage">
  <section class="card card--back" aria-label="Business card back">
    <p class="tagline-top">A REFERRAL FROM YOU IS OUR GREATEST COMPLIMENT</p>
    <p class="wordmark">MRF Accountants</p>
    <p class="tagline-bottom">THE END TO YOUR TAX PROBLEMS <strong>BEGIN WITH US</strong></p>
  </section>

  <section class="card card--front" aria-label="Business card front">
    <p class="wordmark">MRF Accountants</p>
    <div class="rule"></div>
    <div class="person">
      <p class="person__name">MARCUS ELWIN</p>
      <p class="person__title">Managing Director</p>
      <div class="person__rule"></div>
    </div>
    <ul class="contacts">
      <li>
        <svg viewBox="0 0 24 24" aria-hidden="true"><path d="M6.6 10.8a15.1 15.1 0 0 0 6.6 6.6l2.2-2.2a1 1 0 0 1 1-.25 11.4 11.4 0 0 0 3.6.57 1 1 0 0 1 1 1V20a1 1 0 0 1-1 1A17 17 0 0 1 3 4a1 1 0 0 1 1-1h3.5a1 1 0 0 1 1 1c0 1.25.2 2.45.57 3.57a1 1 0 0 1-.25 1z"/></svg>
        <span>9481 3057</span>
      </li>
      <li>
        <svg viewBox="0 0 24 24" aria-hidden="true"><path d="M2 5h20v14H2z M2 5l10 8 10-8" /></svg>
        <span>melwin@mrfaccountants.com.au</span>
      </li>
    </ul>
    <div class="band band--address">Level 5, 8 Corvale Ridge Road, Ashgrove Rise Vic 3187</div>
    <div class="band band--web">www.mrfaccountants.com.au</div>
  </section>
</main>
</body>
</html>
```